Window cleaning and Pressure washing

Truck wrap partial or full/background:
Would like to see a background of a water mark or something related to window cleaning. And or pressure washing.

Doors of the truck:
Need to have my logo printed in big on the doors and with LLC in small after the logo. Need to have my slogan below my logo on the door.
Slogan is; “Affordable 5 star services!”

Sides of the truck:
Want to see window cleaning and Pressure washing on the sides of the truck in big letters with the phone number. Slanted with a shadow effect.
(Would like to see slanted and not slanted) also need to see something that signifies 100% satisfaction or your money back!Preferably a sticker, Or a combination of both. Also need to have residential and commercial somewhere.
Phone number needs to be on here.

Tailgate:
Want to have the services on the back tailgate with the slogan, as well as the 100% money back guarantee sticker.
And the phone number here to!

Back window;
Needs to have the same background as the wrap on the truck or very slimier with the water swiped away Clean with the logo presented as shown in one of the pictures below.

```html
<!DOCTYPE html>
<html lang="en">
<head>
<meta charset="utf-8">
<title>The Clear Path LLC – Truck Wrap</title>
<link href="https://fonts.googleapis.com/css2?family=Anton&family=Montserrat:wght@600;700;800&family=Oswald:wght@500;700&display=swap" rel="stylesheet">
<style>
  :root {
    --sky: #3aa8e8;
    --sky-deep: #1f86d4;
    --sky-light: #6cc3f2;
    --amber: #fba90f;
    --white: #ffffff;
    --ink: #1b1b1b;
    --silver: #e6e6e6;
    --shade: #5a5a5a;
    --star: #f7c400;
  }
  * { box-sizing: border-box; margin: 0; padding: 0; }
  html, body { width: 997px; height: 1200px; overflow: hidden; background: var(--white); }
  .canvas { position: relative; width: 997px; height: 1200px; background: var(--white); font-family: "Montserrat", sans-serif; }

  .panel { position: absolute; overflow: hidden; border-radius: 6px; }
  .water-bg {
    position: absolute; inset: 0;
    background:
      radial-gradient(ellipse at 20% 30%, rgba(255,255,255,.18) 0%, transparent 45%),
      radial-gradient(ellipse at 75% 70%, rgba(255,255,255,.12) 0%, transparent 40%),
      linear-gradient(135deg, var(--sky-light) 0%, var(--sky) 45%, var(--sky-deep) 100%);
  }

  /* Side panel */
  .side { left: 30px; top: 150px; width: 937px; height: 200px; }
  .licensed { position: absolute; left: 85px; top: 22px; color: var(--white); font-weight: 700; font-size: 15px; letter-spacing: .2px; }
  .licensed .band { display: block; margin-top: 3px; background: var(--amber); padding: 1px 0 1px 8px; width: 124px; letter-spacing: 5px; font-size: 14px; }

  .logo { position: absolute; left: 262px; top: 34px; color: var(--white); font-weight: 800; line-height: .92; }
  .logo .l1 { font-size: 24px; display: block; }
  .logo .l2 { font-size: 38px; display: block; padding-left: 10px; }
  .logo .l3 { font-size: 24px; display: block; padding-left: 48px; }
  .logo .llc { font-size: 12px; margin-left: 6px; }

  .slogan-top { position: absolute; left: 228px; top: 123px; width: 218px; height: 24px; background: var(--amber); clip-path: polygon(0 0, 94% 0, 100% 100%, 0 100%); color: var(--white); font-weight: 800; font-size: 19px; padding-left: 40px; line-height: 24px; }
  .slogan-bottom { position: absolute; left: 257px; top: 149px; width: 363px; height: 28px; background: var(--sky-deep); color: var(--white); font-weight: 800; font-size: 21px; line-height: 28px; padding-left: 28px; }

  .headline { position: absolute; left: 490px; top: 20px; font-family: "Anton", sans-serif; font-weight: 400; font-size: 29px; line-height: 31px; color: var(--silver); letter-spacing: 1px; text-shadow: 2px 2px 0 var(--shade); }

  .phone-band { position: absolute; left: 626px; top: 8px; width: 311px; height: 44px; background: var(--amber); clip-path: polygon(4% 0, 100% 0, 100% 100%, 0 100%); }
  .phone-icon { position: absolute; width: 32px; height: 32px; }
  .side .phone-icon { left: 642px; top: 14px; }
  .phone-num { position: absolute; font-family: "Anton", sans-serif; color: var(--silver); text-shadow: 2px 2px 0 var(--shade); letter-spacing: 1px; white-space: nowrap; }
  .side .phone-num { left: 680px; top: 6px; font-size: 34px; }
  .market-pill { position: absolute; left: 690px; top: 54px; width: 187px; height: 18px; background: var(--white); color: var(--sky-deep); font-weight: 700; font-size: 11.5px; text-align: center; line-height: 18px; }

  .guarantee { position: absolute; width: 72px; text-align: center; }
  .guarantee .pct { font-family: "Anton", sans-serif; color: var(--amber); font-size: 26px; line-height: 28px; text-shadow: 1px 1px 0 var(--shade); }
  .guarantee .tag { background: var(--ink); color: var(--white); font-family: "Oswald", sans-serif; font-size: 7px; line-height: 9px; border-radius: 3px; padding: 2px 2px 3px; border-bottom: 2px solid var(--sky); }
  .guarantee .tag b { display: block; background: var(--white); color: var(--ink); margin-top: 1px; font-weight: 700; }
  .guarantee .stars { color: var(--star); font-size: 8px; letter-spacing: 2px; margin-top: 2px; }
  .side .guarantee { left: 828px; top: 80px; }

  .follow { position: absolute; left: 845px; top: 150px; color: var(--white); font-size: 7px; font-weight: 600; text-align: center; width: 40px; }
  .follow .dots { display: flex; justify-content: center; gap: 5px; margin-top: 3px; }
  .follow .dots span { width: 11px; height: 11px; border-radius: 50%; background: var(--white); }

  /* Back window */
  .rear-window { left: 258px; top: 560px; width: 480px; height: 90px; border-radius: 30px 30px 0 0; }
  .rear-window .wiped { position: absolute; right: 0; top: 0; width: 190px; height: 100%; background: linear-gradient(120deg, #c9d2da 0%, #8d9aa6 55%, #e8eef2 100%); clip-path: polygon(22% 0, 100% 0, 100% 100%, 0 100%); }
  .rear-window .logo { left: 30px; top: 12px; }
  .rear-window .logo .l1 { font-size: 24px; }
  .rear-window .logo .l2 { font-size: 36px; }

  /* Tailgate */
  .tailgate { left: 198px; top: 660px; width: 600px; height: 232px; border-radius: 4px; }
  .services { position: absolute; top: 24px; list-style: none; font-family: "Anton", sans-serif; font-size: 19px; line-height: 31px; color: var(--silver); text-shadow: 2px 2px 0 var(--shade); letter-spacing: .5px; }
  .services li { display: flex; align-items: center; gap: 8px; }
  .services svg { width: 17px; height: 17px; flex: none; }
  .services.left { left: 24px; }
  .services.right { left: 378px; }

  .gate-band { position: absolute; left: 0; top: 157px; width: 600px; height: 75px; background: var(--white); }
  .gate-band .blue { position: absolute; left: 0; top: 0; width: 70px; height: 100%; background: var(--sky); }
  .gate-band .orange { position: absolute; left: 55px; top: 0; width: 440px; height: 100%; background: var(--amber); clip-path: polygon(0 100%, 6% 0, 93% 0, 100% 100%); }
  .tailgate .phone-icon { left: 22px; top: 170px; width: 48px; height: 48px; }
  .tailgate .phone-num { left: 92px; top: 160px; font-size: 50px; }
  .tailgate .guarantee { left: 500px; top: 134px; width: 84px; }
  .tailgate .guarantee .pct { font-size: 30px; line-height: 32px; }
  .tailgate .guarantee .tag { font-size: 8px; line-height: 10px; }
</style>
</head>
<body>
<div class="canvas">

  <section class="panel side">
    <div class="water-bg" role="img" aria-label="Blue background covered in water droplets"></div>

    <p class="licensed">LICENSED AND<span class="band">INSURED</span></p>

    <div class="logo">
      <span class="l1">THE</span>
      <span class="l2">CLEAR</span>
      <span class="l3">PATH<span class="llc">LLC</span></span>
    </div>

    <div class="slogan-top">AFFORDABLE</div>
    <div class="slogan-bottom">5 STAR SERVICES!</div>

    <h1 class="headline">WINDOW<br>CLEANING AND<br>PRESSURE<br>WASHING</h1>

    <div class="phone-band"></div>
    <svg class="phone-icon" viewBox="0 0 32 32" aria-hidden="true">
      <circle cx="16" cy="16" r="14" fill="var(--sky-deep)" stroke="var(--white)" stroke-width="2.5"/>
      <path d="M11 8.5c1-.6 1.8-.2 2.3.8l1.2 2.6c.4.8.1 1.5-.6 2l-1 .7c.8 2 2.4 3.6 4.4 4.4l.7-1c.5-.7 1.2-1 2-.6l2.6 1.2c1 .5 1.4 1.3.8 2.3-1 1.6-2.7 2.4-4.7 1.8-4.4-1.3-7.7-4.6-9-9-.6-2 .2-3.7 1.3-4.5z" fill="var(--white)"/>
    </svg>
    <p class="phone-num">(555) 014-2288</p>
    <p class="market-pill">Commercial &amp; Residential</p>

    <div class="guarantee">
      <p class="pct">100%</p>
      <p class="tag">SATISFACTION OR<b>YOUR MONEY BACK!</b></p>
      <p class="stars">★★★★★</p>
    </div>

    <div class="follow">Follow Us<div class="dots"><span></span><span></span></div></div>
  </section>

  <section class="panel rear-window">
    <div class="water-bg" role="img" aria-label="Blue background covered in water droplets"></div>
    <div class="wiped" role="img" aria-label="Wiped-clean window revealing a house behind the glass"></div>
    <div class="logo">
      <span class="l1">THE</span>
      <span class="l2">CLEAR</span>
    </div>
  </section>

  <section class="panel tailgate">
    <div class="water-bg" role="img" aria-label="Blue background covered in water droplets"></div>

    <ul class="services left">
      <li><svg viewBox="0 0 18 18" aria-hidden="true"><circle cx="9" cy="9" r="7.5" fill="var(--white)" stroke="var(--amber)" stroke-width="2"/><path d="M5.5 9.2l2.4 2.3 4.6-4.8" fill="none" stroke="var(--amber)" stroke-width="2"/></svg>WINDOW CLEANING</li>
      <li><svg viewBox="0 0 18 18" aria-hidden="true"><circle cx="9" cy="9" r="7.5" fill="var(--white)" stroke="var(--amber)" stroke-width="2"/><path d="M5.5 9.2l2.4 2.3 4.6-4.8" fill="none" stroke="var(--amber)" stroke-width="2"/></svg>HOUSE WASHING</li>
      <li><svg viewBox="0 0 18 18" aria-hidden="true"><circle cx="9" cy="9" r="7.5" fill="var(--white)" stroke="var(--amber)" stroke-width="2"/><path d="M5.5 9.2l2.4 2.3 4.6-4.8" fill="none" stroke="var(--amber)" stroke-width="2"/></svg>PRESSURE WASHING</li>
    </ul>
    <ul class="services right">
      <li><svg viewBox="0 0 18 18" aria-hidden="true"><circle cx="9" cy="9" r="7.5" fill="var(--white)" stroke="var(--amber)" stroke-width="2"/><path d="M5.5 9.2l2.4 2.3 4.6-4.8" fill="none" stroke="var(--amber)" stroke-width="2"/></svg>ROOF CLEANING</li>
      <li><svg viewBox="0 0 18 18" aria-hidden="true"><circle cx="9" cy="9" r="7.5" fill="var(--white)" stroke="var(--amber)" stroke-width="2"/><path d="M5.5 9.2l2.4 2.3 4.6-4.8" fill="none" stroke="var(--amber)" stroke-width="2"/></svg>GUTTER CLEANING</li>
      <li><svg viewBox="0 0 18 18" aria-hidden="true"><circle cx="9" cy="9" r="7.5" fill="var(--white)" stroke="var(--amber)" stroke-width="2"/><path d="M5.5 9.2l2.4 2.3 4.6-4.8" fill="none" stroke="var(--amber)" stroke-width="2"/></svg>SCREEN REPAIRS</li>
    </ul>

    <div class="gate-band"><div class="blue"></div><div class="orange"></div></div>
    <svg class="phone-icon" viewBox="0 0 32 32" aria-hidden="true">
      <circle cx="16" cy="16" r="14" fill="var(--amber)" stroke="var(--white)" stroke-width="2.5"/>
      <path d="M11 8.5c1-.6 1.8-.2 2.3.8l1.2 2.6c.4.8.1 1.5-.6 2l-1 .7c.8 2 2.4 3.6 4.4 4.4l.7-1c.5-.7 1.2-1 2-.6l2.6 1.2c1 .5 1.4 1.3.8 2.3-1 1.6-2.7 2.4-4.7 1.8-4.4-1.3-7.7-4.6-9-9-.6-2 .2-3.7 1.3-4.5z" fill="var(--white)"/>
    </svg>
    <p class="phone-num">(555) 014-2288</p>

    <div class="guarantee">
      <p class="pct">100%</p>
      <p class="tag">SATISFACTION OR<b>YOUR MONEY BACK!</b></p>
      <p class="stars">★★★★★</p>
    </div>
  </section>

</div>
</body>
</html>
```